Podiatry (services) Business Card

I need a business design for a New Podiatry Service.
the Podiatry services will include all aspects of podiatry including;
general podiatry for all ages
corns and callus treatment
Ingrown toenails & nail surgery
Forefoot, arch and heel pain
Gait analysis
Sports Podiatry and Orthotics
Paediatric Assessments
Diabetes Foot Assessment

I would like the back of the card to have space for next appointment day and time.

I would like a nice design that is simple yet catchy. I don't like cluttered business cards. I like things to be simple yet stand out because of the finer details.

I like the colours blue and white but I'm open to other designs that have different colours.

Industry/Entity Type

Business

Contact Information for Business Card

Cobaltline Podiatry (Business name)

Delphine Marrow - Podiatrist
M.Pod.P., B.Hlth. Sci, MQFodE

Address: 17 Tolbrook Rd, Fernmere East Vic, 3168
Phone: (03) 9462 3178
Fax: (03) 9514 2683

```html
<!DOCTYPE html>
<html lang="en">
<head>
<meta charset="utf-8">
<title>Cobaltline Podiatry – Business Card</title>
<link href="https://fonts.googleapis.com/css2?family=Source+Sans+3:wght@400;600;700&display=swap" rel="stylesheet">
<style>
  :root {
    --brand-blue: #1a7bc6;
    --ink: #111111;
    --card: #ffffff;
    --stage-top: #2b2b2b;
    --stage-bottom: #060606;
    --divider: #cfe0ee;
  }
  * { box-sizing: border-box; margin: 0; padding: 0; }
  html, body { width: 1200px; height: 900px; overflow: hidden; }
  body {
    position: relative;
    background: linear-gradient(180deg, var(--stage-top) 0%, #141414 55%, var(--stage-bottom) 100%);
    font-family: "Source Sans 3", "Myriad Pro", Arial, sans-serif;
    color: var(--ink);
  }
  .card {
    position: absolute;
    top: 306px;
    width: 440px;
    height: 271px;
    background: var(--card);
    border-radius: 12px;
  }
  .card--front { left: 149px; }
  .card--back { left: 608px; border-radius: 12px 12px 0 0; }

  /* Front */
  .brand-name {
    position: absolute;
    left: 24px;
    top: 140px;
    width: 190px;
    text-align: center;
    color: var(--brand-blue);
    font-weight: 400;
    line-height: 1.05;
  }
  .brand-name__main { display: block; font-size: 27px; letter-spacing: 0.5px; }
  .brand-name__sub { display: block; font-size: 17px; letter-spacing: 1px; margin-top: 4px; }
  .divider {
    position: absolute;
    left: 222px;
    top: 64px;
    width: 1px;
    height: 142px;
    background: linear-gradient(180deg, transparent, var(--divider) 20%, var(--divider) 80%, transparent);
  }
  .contact { position: absolute; left: 240px; top: 63px; }
  .contact__name { font-size: 16px; font-weight: 600; color: var(--brand-blue); line-height: 22px; }
  .contact__role { font-size: 12.5px; font-weight: 400; color: var(--ink); }
  .contact__creds { font-size: 12.5px; line-height: 16px; }
  .contact__address { font-size: 12.5px; line-height: 18px; margin-top: 13px; }
  .contact__phones { list-style: none; margin-top: 18px; font-size: 12.5px; line-height: 18px; }
  .contact__phones li { display: flex; align-items: center; gap: 5px; }
  .contact__phones svg { width: 9px; height: 9px; fill: var(--brand-blue); }

  /* Back */
  .back-brand {
    position: absolute;
    left: 20px;
    top: 60px;
    width: 175px;
    text-align: center;
    color: var(--brand-blue);
    font-weight: 400;
    font-size: 24px;
    line-height: 1.15;
  }
  .services {
    position: absolute;
    left: 214px;
    top: 32px;
    list-style: none;
    font-size: 12.8px;
    font-weight: 600;
    line-height: 18.2px;
  }
  .services li { position: relative; padding-left: 11px; }
  .services li::before {
    content: "";
    position: absolute;
    left: 0;
    top: 6px;
    width: 6px;
    height: 6px;
    border-radius: 50%;
    background: var(--brand-blue);
  }
  .appointment__title {
    position: absolute;
    left: 0;
    top: 196px;
    width: 440px;
    text-align: center;
    color: var(--brand-blue);
    font-size: 14.5px;
    font-weight: 600;
  }
  .appointment__fields {
    position: absolute;
    left: 37px;
    top: 233px;
    display: flex;
    gap: 4px;
    font-size: 12px;
    font-weight: 600;
    color: var(--brand-blue);
  }
  .field { display: flex; align-items: flex-end; gap: 3px; }
  .field__line { border-bottom: 2px dotted var(--ink); height: 12px; margin-bottom: 2px; }
  .field--name .field__line { width: 106px; }
  .field--date .field__line { width: 72px; }
  .field--time .field__line { width: 74px; }
</style>
</head>
<body>
  <section class="card card--front" aria-label="Business card front">
    <div class="brand-name">
      <span class="brand-name__main">COBALTLINE</span>
      <span class="brand-name__sub">PODIATRY</span>
    </div>
    <div class="divider"></div>
    <div class="contact">
      <p class="contact__name">Delphine Marrow <span class="contact__role">- Podiatrist</span></p>
      <p class="contact__creds">M.Pod.P., B.Hlth. Sci, MQFodE</p>
      <p class="contact__address">17 Tolbrook Rd, Fernmere<br>East Vic, 3168</p>
      <ul class="contact__phones">
        <li>
          <svg viewBox="0 0 10 10" aria-hidden="true"><path d="M2 0.5 L3.6 2.6 L2.8 3.6 Q4 6 6.4 7.2 L7.4 6.4 L9.5 8 L8.4 9.5 Q2.5 9 0.5 1.6 Z"/></svg>
          (03) 9462 3178
        </li>
        <li>
          <svg viewBox="0 0 10 10" aria-hidden="true"><rect x="2.5" y="0.5" width="5" height="3"/><rect x="0.5" y="4" width="9" height="5.5" rx="1"/></svg>
          (03) 9514 2683
        </li>
      </ul>
    </div>
  </section>

  <section class="card card--back" aria-label="Business card back">
    <div class="back-brand">Cobaltline<br>Podiatry</div>
    <ul class="services">
      <li>General podiatry for all ages</li>
      <li>Corns and callus treatment</li>
      <li>Ingrown toenails &amp; nail surgery</li>
      <li>Forefoot, arch and heel pain</li>
      <li>Gait analysis</li>
      <li>Sports Podiatry and Orthotics</li>
      <li>Paediatric Assessments</li>
      <li>Diabetes Foot Assessment</li>
    </ul>
    <p class="appointment__title">Appointment</p>
    <div class="appointment__fields">
      <div class="field field--name">Name: <span class="field__line"></span></div>
      <div class="field field--date">Date: <span class="field__line"></span></div>
      <div class="field field--time">Time: <span class="field__line"></span></div>
    </div>
  </section>
</body>
</html>
```